wig manufacturer
I would like something very upscale.highend looking
maybe mat chrome card with shiney chrome
or something like the Quince business card very clean and simple white with the logo in silver
Target Market(s)
upscale women
Industry/Entity Type
Business
Contact Information for Business Card
OUR LOGO
company name:Rosamund Wigs
48E92Avenue Harold Pinsett
New York,N.Y 10018
Tel:212-5550148
1800-5550193
email:tressline@mailbox.example
website:Rosamundwigs.example

```html
<!DOCTYPE html>
<html lang="en">
<head>
<meta charset="utf-8">
<title>Rosamund Wigs – Business Card</title>
<link rel="stylesheet" href="https://fonts.googleapis.com/css2?family=Arimo:wght@400;700&display=swap">
<style>
  :root {
    --stage: #1c1c1e;
    --card: #ffffff;
    --navy: #2e4a8c;
    --ink: #222428;
    --muted: #55585e;
  }
  * { box-sizing: border-box; margin: 0; padding: 0; }
  html, body { width: 1200px; height: 908px; overflow: hidden; }
  body {
    background: var(--stage);
    font-family: "Arimo", Arial, sans-serif;
    position: relative;
  }
  .card {
    position: absolute;
    width: 560px;
    height: 320px;
    background: var(--card);
    border-radius: 22px;
    overflow: hidden;
    box-shadow: 0 18px 40px rgba(0,0,0,0.55);
  }
  .card--front { left: 90px; top: 110px; }
  .card--back  { left: 550px; top: 478px; }

  .brand {
    display: flex;
    align-items: center;
    gap: 14px;
    color: var(--navy);
    font-weight: 400;
    letter-spacing: 0.5px;
  }
  .brand__mark {
    background: var(--navy);
    flex: none;
  }
  .card--front .brand {
    position: absolute;
    left: 0; right: 0; top: 0; bottom: 0;
    justify-content: center;
    font-size: 58px;
  }
  .card--front .brand__mark { width: 64px; height: 64px; }

  .card--back .brand {
    position: absolute;
    right: 40px;
    top: 32px;
    font-size: 32px;
  }
  .card--back .brand__mark { width: 30px; height: 30px; }

  .person {
    position: absolute;
    left: 36px;
    top: 84px;
    padding-left: 12px;
    border-left: 4px solid var(--navy);
  }
  .person__name {
    color: var(--navy);
    font-weight: 700;
    font-size: 20px;
    line-height: 1.15;
    letter-spacing: 0.5px;
  }
  .person__role {
    color: var(--muted);
    font-size: 13px;
    margin-top: 3px;
    letter-spacing: 0.4px;
  }
  .contact {
    position: absolute;
    left: 36px;
    top: 146px;
    color: var(--ink);
    font-size: 14px;
    line-height: 1.3;
  }
  .contact__phone { font-weight: 700; font-size: 16px; }
  .contact__address { margin-top: 10px; }
  .card__band {
    position: absolute;
    left: 0; right: 0; bottom: 0;
    height: 38px;
    background: var(--navy);
  }
</style>
</head>
<body>
  <section class="card card--front" aria-label="Business card front">
    <div class="brand">
      <span class="brand__mark"></span>
      <span class="brand__name">rosamund</span>
    </div>
  </section>

  <section class="card card--back" aria-label="Business card back">
    <div class="brand">
      <span class="brand__mark"></span>
      <span class="brand__name">rosamund</span>
    </div>
    <div class="person">
      <p class="person__name">HAROLD PINSETT</p>
      <p class="person__role">GENERAL MANAGER</p>
    </div>
    <div class="contact">
      <p class="contact__phone">212-5550148</p>
      <p>tressline@mailbox.example</p>
      <p>Rosamundwigs.example</p>
      <p class="contact__address">48E92Avenue,<br>New York, N.Y 10018</p>
    </div>
    <div class="card__band"></div>
  </section>
</body>
</html>
```